Brindle Press Promotional Brochure

www.brindlepress-demo.com

Award Winning Trade Printer

Refer to website and create a Brochure 5 colour using metallic gold 871
Images can be supplied hi resolution from website if required or further images

Using the following titles
Specialising in High Quality Trade Printing Nationally
Books, Catalogues, Booklets
Brochures, Flyers and Mail Outs
Presentation Folders
Business Cards and Stationery
Also Specialising in
Labels and Packaging
print and engineering from original concept packaging

Come and see our friendly staff or visit our website
Compare our prices via email

Target Market(s)

Print Buyers

Industry/Entity Type

Printing

Requirements
Must have
• a pms Gold included in final artwork
• A Premium/Quality/upmarket approach
• Hi Quality IMAGES etc.
• I placed an image of an awards dinner BUT that is just there for a personal image not essential to have by any means
Nice to have
• Sections in the brochure for each type of print or panel with a cover page wow!!! BRINDLE!
Should not have
• poor quality images

```html
<!DOCTYPE html>
<html lang="en">
<head>
<meta charset="utf-8">
<title>Brindle Press – Tri-fold Brochure</title>
<link href="https://fonts.googleapis.com/css2?family=Encode+Sans+Semi+Condensed:wght@400;600;700&family=Montserrat:wght@300;400&family=Allura&display=swap" rel="stylesheet">
<style>
:root{
  --black:#0b0b0b;
  --ink:#222;
  --white:#fff;
  --gold:#a08a3d;
  --gold-dark:#76642a;
  --gold-light:#dcc77e;
  --gold-text:#c9a93f;
  --paper:#ffffff;
  --grey:#5a5a5a;
}
*{box-sizing:border-box;margin:0;padding:0}
html,body{width:848px;height:1200px;overflow:hidden;background:var(--paper)}
body{position:relative;font-family:"Encode Sans Semi Condensed",Arial,sans-serif;color:var(--ink)}
.abs{position:absolute}
.spread{position:absolute;left:111px;width:611px;box-shadow:3px 4px 8px rgba(0,0,0,.35);overflow:hidden}

/* outside spread */
.outside{top:111px;height:432px;background:var(--black)}
.panel{position:absolute;top:0;height:419px}
.panel-about{left:0;width:205px;background:var(--black)}
.panel-about .lower{position:absolute;left:0;top:190px;width:205px;height:229px;background:var(--white)}
.panel-about .fade{position:absolute;left:0;top:160px;width:205px;height:60px;background:linear-gradient(180deg,var(--black),#777 45%,var(--white))}
.headline{position:absolute;left:0;top:48px;width:205px;text-align:center;color:var(--white);font-weight:700;font-size:19px;line-height:1.2}
.photo-circle{position:absolute;border-radius:50%;border:4px solid var(--gold);overflow:hidden}
.photo-press{left:58px;top:118px;width:146px;height:146px;background:radial-gradient(circle at 40% 40%,#e6e04a,#b8b52c 35%,#6d6d66 65%,#3a3a3a)}
.section-title{display:flex;align-items:center;gap:4px;font-weight:700;font-size:11.5px;color:var(--black)}
.section-title::before{content:"";width:9px;height:9px;background:var(--gold)}
.about-title{position:absolute;left:31px;top:253px}
.body-copy{font-size:5.7px;line-height:1.38;color:var(--ink)}
.body-copy p{margin-bottom:6px}
.about-copy{position:absolute;left:31px;top:270px;width:158px}

.panel-contact{left:205px;width:202px;background:var(--black);border-left:1px solid #222;border-right:1px solid #222;text-align:center;color:var(--white)}
.spaced{font-family:"Montserrat",Arial,sans-serif;font-weight:300;letter-spacing:.42em}
.contact-name{position:absolute;left:0;width:202px;top:222px;font-size:15px;line-height:1.25;padding-left:.42em}
.contact{position:absolute;left:0;width:202px;top:275px;font-size:7.4px;line-height:1.45}
.contact .lead{font-weight:700;font-size:8px;margin-bottom:6px}
.contact .addr{color:#ccc}
.contact b{font-weight:700}
.contact .web{color:var(--gold-text);font-weight:700}
.find{position:absolute;left:0;width:202px;top:378px;font-size:8px;font-weight:700;display:flex;justify-content:center;align-items:center;gap:6px}
.find span.sq{width:13px;height:13px;background:var(--white)}

.panel-cover{left:407px;width:204px;background:var(--black)}
.cover-gold{position:absolute;left:0;top:190px;width:204px;height:229px;background:linear-gradient(180deg,rgba(160,138,61,0) 0%,var(--gold) 22%,var(--gold) 100%)}
.brand-mark{position:absolute;left:0;top:92px;width:204px;text-align:center;color:var(--white);font-size:17px}
.brand-mark .dot{display:inline-block;width:9px;height:9px;border-radius:50%;background:var(--white);margin-right:6px;vertical-align:2px}
.brand-sub{position:absolute;left:0;top:146px;width:204px;text-align:center;color:var(--white);font-size:15px;padding-left:.42em}
.badge{position:absolute;left:112px;top:250px;width:78px;height:78px;border-radius:50%;background:radial-gradient(circle at 40% 35%,#f3e3a0,#c9a94c 55%,#8a7230);border:3px solid var(--black);box-shadow:0 0 0 2px var(--gold-light);display:flex;align-items:center;justify-content:center;text-align:center;font-weight:700;font-size:11px;line-height:1.05;color:var(--black)}
.tagline{position:absolute;left:0;top:354px;width:204px;text-align:center;color:var(--white);font-size:10.5px;font-weight:600}
.outside .base{position:absolute;left:0;top:419px;width:611px;height:13px;background:var(--black);border-top:1px solid #333}

/* inside spread */
.inside{top:567px;height:431px;background:var(--gold)}
.banner{position:absolute;left:0;top:0;width:437px;height:96px;background:linear-gradient(180deg,var(--gold) 0%,var(--gold) 28%,#3d3419 62%,var(--black) 100%)}
.banner h2{position:absolute;left:32px;top:37px;color:var(--white);font-weight:600;font-size:12.5px}
.content{position:absolute;left:0;top:96px;width:437px;height:299px;background:var(--white)}
.col{position:absolute;top:18px;width:160px}
.col-quality{left:32px}
.col-printing{left:223px;top:18px}
.col .section-title{margin-bottom:5px}
.col .body-copy p{margin-bottom:5px}
.book{position:absolute;left:454px;top:18px;width:130px;height:108px;background:linear-gradient(160deg,#f1f1ef 0%,#cfcfcf 35%,#8a6a4f 55%,#3f4d6b 75%,#6e5b3c 100%);clip-path:polygon(18% 8%,100% 0,92% 78%,10% 100%)}
.thumb{position:absolute;width:76px;height:76px;border-radius:50%;border:3px solid var(--white);box-shadow:0 0 0 2px var(--gold-dark),2px 3px 5px rgba(0,0,0,.4)}
.t1{left:392px;top:80px;background:radial-gradient(circle at 45% 45%,#f2f2f2,#bdbdbd 60%,#2f3a32)}
.t2{left:392px;top:157px;background:linear-gradient(135deg,#e8a22a,#5a4a3b 50%,#f1f1f1)}
.t3{left:392px;top:236px;background:radial-gradient(circle at 50% 55%,#2a2a2a,#6a5a4a 70%,#d9d2c4)}
.t4{left:392px;top:313px;background:radial-gradient(circle at 50% 50%,#b3261e 0 14%,#f2f0ea 16%,#d9d5cc 80%)}
.specialise{position:absolute;left:440px;top:138px;width:171px;text-align:center;color:var(--white);font-family:"Allura",cursive;font-size:21px}
.services{position:absolute;left:460px;top:170px;width:134px;list-style:none;text-align:center;color:var(--white);font-weight:600;font-size:8px;line-height:1.05}
.services li{border-bottom:1px solid rgba(255,255,255,.35);padding:3.6px 0}
.services li:last-child{border-bottom:none}
.footer{position:absolute;left:0;top:395px;width:611px;height:23px;background:var(--black);color:var(--white);font-weight:700;font-style:italic;font-size:8px;text-align:center;line-height:23px;padding-right:40px}
.inside .strip{position:absolute;left:0;top:418px;width:611px;height:13px;background:var(--gold)}

.label-bar{position:absolute;left:0;top:1100px;width:848px;height:40px;background:var(--black);color:var(--white);font-weight:700;font-size:15px;text-align:right;padding-right:142px;line-height:40px}
</style>
</head>
<body>

<section class="spread outside" aria-label="Brochure outside">
  <div class="panel panel-about">
    <div class="lower"></div>
    <div class="fade"></div>
    <h1 class="headline">Printing is more<br>than a job<br>- it is an artform.</h1>
    <div class="photo-circle photo-press" role="img" aria-label="Close-up photo of a printing press roller with yellow ink"></div>
    <h3 class="section-title about-title">About Us</h3>
    <div class="body-copy about-copy">
      <p>Brindle Press takes great pride in our craftsmanship, skill and ingenuity to ensure we deliver the best possible printing outcome for every job.</p>
      <p>Known widely as a 'printer's printer' there is no job too small, large or complex for Brindle Press from your smallest business card run through to the most intricate and difficult printing task.</p>
      <p>Renown for high quality of work, state-of-the-art technology and commitment to excellence, Brindle have worked hard to be established as one of the premier printers in Tasmania.</p>
    </div>
  </div>

  <div class="panel panel-contact">
    <div class="spaced contact-name">BRINDLE<br>PRESS</div>
    <div class="contact">
      <p class="lead">Call us or email for a quote:</p>
      <p class="addr">18 Kestrel Lane<br>Northgate , Tasmania</p>
      <p><b>p. (03) 6000 4821</b></p>
      <p class="addr">f. (03) 6000 4822</p>
      <p><b>e. print@brindlepress-demo.com</b></p>
      <p class="web">www.brindlepress-demo.com</p>
    </div>
    <div class="find">Find us on <span class="sq"></span></div>
  </div>

  <div class="panel panel-cover">
    <div class="cover-gold"></div>
    <div class="spaced brand-mark"><span class="dot"></span>BRINDLE</div>
    <div class="spaced brand-sub">PRESS</div>
    <div class="badge">Award<br>Winning<br>Trade<br>Printer</div>
    <p class="tagline">For the finest of impressions</p>
  </div>
  <div class="base"></div>
</section>

<section class="spread inside" aria-label="Brochure inside">
  <div class="banner"><h2>Our quality is our trademark.</h2></div>
  <div class="content">
    <div class="col col-quality">
      <h3 class="section-title">Quality</h3>
      <div class="body-copy">
        <p>Brindle Press is a Tasmanian institution.</p>
        <p>With humble beginnings starting in the family home in 1978 before moving to the premises where you can find us today, Brindle Press has always been a market leader and committed to printing of the highest distinction.</p>
        <p>Strong family traditions have conveyed particular Brindle Press skills and craftsmanship through the decades including complex tricks of the trade that are learnt, practiced and refined in-house to build a reputation of superiority and brilliance.</p>
        <p>In fact, Brindle was the first Tasmanian owned company to install a four-colour process offset Press in Tasmania back in 1992 and have a continual goal for improvement and excellence in every job done.</p>
        <p>Today, a new addition to the family is a new five-colour and Aqueous coating. This offset press has delivered even faster and higher quality work for clients.</p>
      </div>
      <h3 class="section-title" style="margin-top:4px">Awards</h3>
      <div class="body-copy">
        <p>Brindle Press prides itself on its commitment to quality and exceptional printing practices and technologies delivering the best printing outcome for each unique task.</p>
        <p>The Brindle Press way, craft and capabilities in fine print have been extensively recognised locally and nationally through a number of awards recognising industry quality and excellence.</p>
      </div>
    </div>

    <div class="col col-printing">
      <h3 class="section-title">Printing</h3>
      <div class="body-copy">
        <p>Every print job is unique and every print job requires specialist care, attention and skill.</p>
        <p>Brindle Press delivers beyond the call of duty for every job.</p>
        <p>The Brindle Press team will work with you to create more than just a print job but an artform.</p>
        <p>Brindle Press specialises in the highest quality offset printing with ongoing improvement to our capital investment ensuring we remain at the leading edge of printing in Tasmania.</p>
        <p>Our high-speed printing capabilities, innovative technology and master craftsmanship means we can print just about anything you can create!</p>
        <p>The Brindle Press team will capably manage the printing task at hand for a range of mediums from small print runs to large scale production.</p>
        <p>Our 5 colour and Aqueous coating offset press is the latest addition delivering even faster and higher quality printing solutions.</p>
        <p>Brindle Press can run four colour plus spot and coating all in the one pass delivering economical and quality benefits for customers. This advanced technology and capability to deliver brilliance in colour, manage varied sheet sizes, inline coating mechanisms and other time saving functions means your job is printed with quality, efficiency and speed.</p>
        <p>Our aim is to provide our customers with consistent printing quality and excellence for a competitive price.</p>
        <p>Get optimum results for your next print job. Request a quote today.</p>
      </div>
    </div>
  </div>

  <div class="book" role="img" aria-label="Photo of a stack of printed books with coloured spines"></div>
  <div class="thumb t1" role="img" aria-label="Photo of a presentation folder"></div>
  <div class="thumb t2" role="img" aria-label="Photo of printed booklet covers"></div>
  <div class="thumb t3" role="img" aria-label="Photo of a dark printed catalogue"></div>
  <div class="thumb t4" role="img" aria-label="Photo of printed stationery"></div>

  <p class="specialise">We specialise in</p>
  <ul class="services">
    <li>High Quality<br>Trade Printing Nationally</li>
    <li>Books</li>
    <li>Catalogues</li>
    <li>Booklets</li>
    <li>Brochures</li>
    <li>Flyers</li>
    <li>Mail Outs</li>
    <li>Presentation Folders</li>
    <li>Business Cards<br>and Stationery</li>
    <li>Labels and Packaging</li>
    <li>Print and engineering<br>from original concept<br>packaging</li>
  </ul>

  <div class="footer">Come and see our friendly staff or visit our website - compare our prices via email</div>
  <div class="strip"></div>
</section>

<div class="label-bar">TRI-FOLD BROCHURE</div>

</body>
</html>
```